Nebelkreis - needs a CD/Cover Design for a VA Compilation

We need a CD-Design/Cover-Artwork for our Various Artists Compilation called 'Nebelkreis', which means "Fog circle". Back then our events were based in one of Germanys best underground techno-clubs., which we also called "our temple".
The artists featured on this compilation rather performed at our events or had a massive influence on the music the djs played.
The sound is glitchy, technically detailed and a little unpredictable.

We would like to see some designs not too colourful!

Target Market(s)

complex electronic music listeners

Industry/Entity Type

Club

Font styles to use
Sans Serif

Colors
ec1f27

Requirements
Must have
• Ideally the artwork should be something otherworldly, abstract/glitchy, be an optical illusion and/or have geometric complexity.
Nice to have
• - probably black and white design fits better with us, but you can also try it with a very few colors.
- maybe something futuristic or scatchy
Should not have
• - it should definitely NOT be too colourful.
- no humans!! or animals
- in case you think to draw a temple, please use it more abstract, nothing too obviously, we dont wanna look like a hippie event!
- no musical notes
- no obvious "play" symbol / headphones or vinyl images

```html
<!DOCTYPE html>
<html lang="de">
<head>
<meta charset="utf-8">
<title>Nebelkreis – VA Compilation Cover</title>
<link rel="stylesheet" href="https://fonts.googleapis.com/css2?family=Michroma&display=swap">
<style>
  :root {
    --cover-black: #0b0b0b;
    --mesh-light: #8a8a8a;
    --mesh-mid: #4a4a4a;
    --mesh-dark: #1a1a1a;
    --title-white: #ffffff;
    --glitch-red: #ec1f27;
    --glitch-cyan: #19c7c2;
  }
  html, body {
    margin: 0;
    padding: 0;
    width: 1200px;
    height: 1200px;
    overflow: hidden;
    background: var(--cover-black);
  }
  .cover {
    position: relative;
    width: 1200px;
    height: 1200px;
    background: var(--cover-black);
    overflow: hidden;
  }
  .wave-field {
    position: absolute;
    inset: 0;
    width: 1200px;
    height: 1200px;
    display: block;
  }
  .compilation-title {
    position: absolute;
    top: 486px;
    right: 91px;
    margin: 0;
    font-family: "Michroma", sans-serif;
    font-weight: 400;
    font-size: 48px;
    line-height: 1;
    letter-spacing: 1px;
    color: var(--title-white);
    text-transform: uppercase;
    text-shadow:
      -9px 2px 0 var(--glitch-red),
      3px -1px 0 var(--glitch-cyan);
    white-space: nowrap;
  }
</style>
</head>
<body>
  <main class="cover">
    <svg class="wave-field" viewBox="0 0 1200 1200" role="img" aria-label="Abstract wireframe mesh of intersecting flowing waves in fine white lines">
      <defs>
        <linearGradient id="meshTone" x1="0" y1="0" x2="0.3" y2="1">
          <stop offset="0" stop-color="var(--mesh-mid)"/>
          <stop offset="0.45" stop-color="var(--mesh-light)"/>
          <stop offset="0.8" stop-color="var(--mesh-mid)"/>
          <stop offset="1" stop-color="var(--mesh-dark)"/>
        </linearGradient>
      </defs>
      <polygon points="0,483 840,718 1200,635 1200,1200 0,1200" fill="url(#meshTone)"/>
    </svg>
    <h1 class="compilation-title">Nebelkreis</h1>
  </main>
</body>
</html>
```